Music Industry Business Needs a Business Card Design

Copper Lantern is an audio mastering company that has been in business for 20 years. Mastering is the final creative step in the music production chain. Our job is to make the music sound as good as it possibly can prior to release to the public. Our world is technical, artistic, precise. We work on everything from independent artists to the music for the Grandfield Cup. We are looking for a new, more modern business card design. I am uploading a copy of our logo, although it doesn't absolutely need to be included in the design.

Target Market(s)

Music Industry Professionals

Industry/Entity Type

Business

Contact Information for Business Card

Address, Phone, Email, Website, Name, Job Title

Font styles to use
Sans Serif

Requirements
Must have
• Sorry, but I don't have any concrete things to request. If I had a clear idea of what I want, I would probably just design something myself. I am looking for fresh input and thought I would try this.
Should not have
• Anything that is typical, such as headphones or the like.

```html
<!DOCTYPE html>
<html lang="en">
<head>
<meta charset="utf-8">
<title>Copper Lantern – Business Card</title>
<link rel="stylesheet" href="https://fonts.googleapis.com/css2?family=Montserrat:wght@700&family=Questrial&display=swap">
<style>
  :root {
    --paper: #ffffff;
    --ink: #1e1e1e;
    --ink-soft: #5a5a5a;
    --band: #1d1d1d;
    --band-text: #ffffff;
    --mint: #66ffb3;
    --indigo: #2a0f80;
    --plum: #5e0a70;
    --orange: #ff7400;
  }
  html, body {
    margin: 0;
    padding: 0;
    overflow: hidden;
    background: var(--paper);
  }
  .card {
    position: relative;
    width: 1200px;
    height: 686px;
    overflow: hidden;
    background: var(--paper);
    font-family: "Questrial", sans-serif;
  }
  .brand-name {
    position: absolute;
    left: 89px;
    top: 120px;
    margin: 0;
    font-family: "Questrial", sans-serif;
    font-weight: 400;
    font-size: 30px;
    line-height: 40px;
    letter-spacing: 0.5px;
    color: var(--ink);
    text-transform: uppercase;
  }
  .person {
    position: absolute;
    left: 63px;
    top: 294px;
    margin: 0;
  }
  .person-name {
    margin: 0;
    font-family: "Montserrat", sans-serif;
    font-weight: 700;
    font-size: 39px;
    line-height: 48px;
    color: var(--ink);
    text-transform: uppercase;
  }
  .person-title {
    margin: 0;
    font-family: "Montserrat", sans-serif;
    font-weight: 700;
    font-size: 27px;
    line-height: 34px;
    color: var(--ink);
    text-transform: uppercase;
  }
  .contacts {
    position: absolute;
    left: 63px;
    top: 394px;
    margin: 0;
    padding: 0;
    list-style: none;
  }
  .contact-item {
    display: flex;
    align-items: center;
    height: 42px;
    font-size: 32px;
    color: var(--ink-soft);
  }
  .contact-dot {
    display: inline-block;
    width: 29px;
    height: 15px;
    border-radius: 8px;
    margin-right: 13px;
  }
  .dot-phone { background: var(--mint); }
  .dot-email { background: var(--indigo); }
  .dot-web { background: var(--plum); }
  .waveform-art {
    position: absolute;
    left: 594px;
    top: 57px;
    width: 606px;
    height: 480px;
    background: linear-gradient(180deg, var(--mint) 0%, var(--plum) 50%, var(--orange) 100%);
    opacity: 0.85;
  }
  .address-band {
    position: absolute;
    left: 0;
    top: 575px;
    width: 1200px;
    height: 111px;
    background: var(--band);
    color: var(--band-text);
    display: flex;
    flex-direction: column;
    justify-content: center;
    align-items: center;
    font-size: 32px;
    line-height: 40px;
  }
  .address-band p { margin: 0; }
</style>
</head>
<body>
  <main class="card">
    <div class="waveform-art" role="img" aria-label="Layered sound-wave pulse illustration in mint, plum and orange"></div>

    <p class="brand-name">Copper Lantern</p>

    <div class="person">
      <h1 class="person-name">Marisol Keane</h1>
      <p class="person-title">Graphic Designer</p>
    </div>

    <ul class="contacts">
      <li class="contact-item"><span class="contact-dot dot-phone"></span>+403 555 0187</li>
      <li class="contact-item"><span class="contact-dot dot-email"></span>studio@copperlantern.ca</li>
      <li class="contact-item"><span class="contact-dot dot-web"></span>www.copperlantern.ca</li>
    </ul>

    <footer class="address-band">
      <p>215 - 8th Avenue S.W.</p>
      <p>Calgary, Alberta, Canada T2p 1b4</p>
    </footer>
  </main>
</body>
</html>
```